Business Card Design Project

We consult with hotels on setting rates and maximizing a revenue strategy

Industry/Entity Type

Business

Contact Information for Business Card

I am not sure what I want. Our company offers high level consulting to hotels around the country but we are also laid back. I would like something that is professional but also shows the laid back side

```html
<!DOCTYPE html>
<html lang="en">
<head>
<meta charset="utf-8">
<title>Riverpoint Revenue Management Solutions – Business Card</title>
<link href="https://fonts.googleapis.com/css2?family=Kaushan+Script&family=Open+Sans:wght@400&display=swap" rel="stylesheet">
<style>
  :root {
    --teal: #2f8a82;
    --teal-light: #6fb6ad;
    --teal-pale: #cfe5e1;
    --brown: #3a2b25;
    --white: #ffffff;
    --ink-light: #d9d2cc;
    --backdrop: #e7e4e0;
  }
  * { margin: 0; padding: 0; box-sizing: border-box; }
  html, body { width: 1200px; height: 878px; overflow: hidden; }
  body {
    background: var(--backdrop);
    position: relative;
  }
  .card {
    position: absolute;
    top: 285px;
    width: 540px;
    height: 309px;
    border-radius: 4px;
    overflow: hidden;
    box-shadow: 0 6px 18px rgba(0,0,0,0.18);
  }
  /* Front */
  .card-front { left: 30px; background: var(--white); }
  .front-stripes { position: absolute; right: 0; top: 0; width: 230px; height: 309px; }
  .landmark-area {
    position: absolute;
    left: 40px;
    top: 28px;
    width: 210px;
    height: 112px;
    background: linear-gradient(135deg, var(--teal-pale), var(--teal-light));
  }
  .company-name {
    position: absolute;
    left: 40px;
    top: 152px;
    font-family: "Open Sans", sans-serif;
    font-weight: 400;
    font-size: 46px;
    line-height: 1.1;
    color: var(--brown);
  }
  .tagline {
    position: absolute;
    left: 42px;
    top: 218px;
    font-family: "Open Sans", sans-serif;
    font-weight: 400;
    font-size: 16px;
    letter-spacing: 0.5px;
    color: var(--teal);
  }
  /* Back */
  .card-back { left: 630px; background: var(--brown); }
  .name-tab {
    position: absolute;
    right: 40px;
    top: 0;
    width: 220px;
    height: 76px;
    background: var(--teal);
    padding: 12px 16px 0;
    color: var(--white);
  }
  .person-name {
    font-family: "Kaushan Script", cursive;
    font-size: 26px;
    line-height: 1.1;
  }
  .person-title {
    font-family: "Open Sans", sans-serif;
    font-size: 12px;
    margin-top: 6px;
    letter-spacing: 0.3px;
  }
  .contact-list {
    position: absolute;
    right: 40px;
    bottom: 48px;
    list-style: none;
    text-align: right;
    font-family: "Open Sans", sans-serif;
    font-size: 13px;
    line-height: 1.75;
    color: var(--ink-light);
  }
  .contact-list .phones { margin-bottom: 6px; }
</style>
</head>
<body>
  <section class="card card-front" aria-label="Card front">
    <svg class="front-stripes" viewBox="0 0 230 309" aria-hidden="true">
      <defs>
        <linearGradient id="stripeFade" x1="0" y1="0" x2="1" y2="1">
          <stop offset="0" stop-color="#cfe5e1"/>
          <stop offset="1" stop-color="#2f8a82"/>
        </linearGradient>
      </defs>
      <polygon points="230,20 230,80 90,309 40,309" fill="url(#stripeFade)"/>
      <polygon points="230,105 230,170 160,309 118,309" fill="url(#stripeFade)"/>
      <polygon points="230,200 230,309 190,309" fill="#2f8a82"/>
    </svg>
    <div class="landmark-area" role="img" aria-label="Illustration of a teal suspension bridge"></div>
    <div class="company-name">Riverpoint</div>
    <div class="tagline">Revenue Management Solutions</div>
  </section>

  <section class="card card-back" aria-label="Card back">
    <div class="name-tab">
      <div class="person-name">Mara Ellison</div>
      <div class="person-title">Regional Revenue Manager</div>
    </div>
    <ul class="contact-list">
      <li>Office: 555-014-2231</li>
      <li class="phones">Fax: 555-014-7789</li>
      <li>Email: Mara@RiverpointRMS.com</li>
      <li>Web: www.RiverpointRMS.com</li>
    </ul>
  </section>
</body>
</html>
```